Business Card Design Project

parking lot sealing and striping company

Industry/Entity Type

Business

Contact Information for Business Card

See pics below, blue and gray colors

```html
<!DOCTYPE html>
<html lang="en">
<head>
<meta charset="utf-8">
<title>Northgate Paving – Business Card</title>
<link rel="stylesheet" href="https://fonts.googleapis.com/css2?family=Oswald:wght@600&family=Roboto:wght@400;500&display=swap">
<style>
  :root {
    --stage: #1a1a1a;
    --card: #fbfbfb;
    --navy: #0f2b3b;
    --blue: #1b9ad8;
    --asphalt: #3b3b3c;
    --white: #ffffff;
  }
  html, body {
    margin: 0;
    width: 1200px;
    height: 767px;
    overflow: hidden;
    background: var(--stage);
  }
  .card {
    position: absolute;
    left: 377px;
    top: 248px;
    width: 446px;
    height: 269px;
    background: var(--card);
    overflow: hidden;
    font-family: "Roboto", sans-serif;
    color: var(--navy);
  }
  .card-wave {
    position: absolute;
    inset: 0;
    width: 446px;
    height: 269px;
  }
  .holder-name {
    position: absolute;
    left: 31px;
    top: 39px;
    margin: 0;
    font-family: "Oswald", sans-serif;
    font-weight: 600;
    font-size: 18px;
    line-height: 1;
    letter-spacing: 0.2px;
  }
  .holder-role {
    position: absolute;
    left: 31px;
    top: 63px;
    margin: 0;
    font-size: 10px;
    font-weight: 500;
  }
  .address {
    position: absolute;
    left: 31px;
    top: 93px;
    margin: 0;
    font-size: 11px;
    font-weight: 500;
  }
  .contacts {
    position: absolute;
    left: 31px;
    top: 116px;
    margin: 0;
    padding: 0;
    list-style: none;
    font-size: 11px;
    font-weight: 500;
  }
  .contacts li {
    display: flex;
    align-items: center;
    height: 16px;
  }
  .contacts svg {
    width: 11px;
    height: 11px;
    margin-right: 9px;
    fill: var(--blue);
  }
  .brand {
    position: absolute;
    left: 222px;
    top: 26px;
    display: flex;
    align-items: center;
  }
  .brand-dot {
    width: 48px;
    height: 48px;
    border-radius: 50%;
    background: var(--navy);
    margin-right: 14px;
  }
  .brand-name {
    font-family: "Roboto", sans-serif;
    font-weight: 500;
    font-size: 22px;
    line-height: 1.05;
    color: var(--blue);
  }
  .services {
    position: absolute;
    right: 23px;
    top: 176px;
    margin: 0;
    padding: 0;
    list-style: none;
    text-align: right;
    color: var(--white);
    font-size: 13px;
    font-weight: 500;
    line-height: 19px;
  }
  .services .mark {
    font-size: 11px;
    margin-right: 6px;
  }
</style>
</head>
<body>
  <section class="card">
    <svg class="card-wave" viewBox="0 0 446 269" aria-hidden="false">
      <path role="img" aria-label="Asphalt surface texture" fill="var(--asphalt)"
            d="M0,186 C80,226 180,240 262,200 C330,166 390,124 446,116 L446,269 L0,269 Z"/>
      <path fill="var(--white)"
            d="M32,196 C110,226 212,224 292,188 C352,160 402,134 446,124 L446,135 C402,146 356,168 302,194 C220,234 110,232 32,196 Z"/>
      <path fill="var(--white)"
            d="M0,212 C70,246 178,254 252,216 C196,250 80,256 0,226 Z"/>
    </svg>

    <h1 class="holder-name">MARCUS HALE</h1>
    <p class="holder-role">Managing Director</p>
    <p class="address">14/3 Ridgeline Court, VIC 3150</p>

    <ul class="contacts">
      <li>
        <svg viewBox="0 0 12 12"><path d="M1 4c0-2 2-3 5-3s5 1 5 3v1H8.5V3.8h-5V5H1z M2.5 6h7l1 5h-9z"/></svg>
        Free Call: 1800 NTH GATE
      </li>
      <li>
        <svg viewBox="0 0 12 12"><path d="M0 2h12v8H0z M1 3l5 4 5-4" stroke="var(--card)" stroke-width="1"/></svg>
        marcus@northgatepaving.com
      </li>
      <li>
        <svg viewBox="0 0 12 12"><circle cx="6" cy="6" r="5.5"/><path d="M0.5 6h11 M6 0.5v11 M2 3h8 M2 9h8" stroke="var(--card)" stroke-width="0.8"/></svg>
        www.northgatepaving.com
      </li>
    </ul>

    <div class="brand">
      <span class="brand-dot"></span>
      <span class="brand-name">Northgate<br>Paving</span>
    </div>

    <ul class="services">
      <li><span class="mark">»</span>Asphal Bealing</li>
      <li><span class="mark">»</span>Crack Repair</li>
      <li><span class="mark">»</span>Ramp Building</li>
      <li><span class="mark">»</span>Line Paiing <span class="mark">»</span>Walevwe</li>
    </ul>
  </section>
</body>
</html>
```